FLYERENTWURF  für Make up Ausbildung
FLYERENTWURF für Make up Ausbildung
Zielgruppe
friseure die sich weiterbilden wollen
Aufgabenstellung
zu entwerfen ist ein doppelseitiger flyer in A4, zweimal gefalten.
außenseite:
erste spalte/deckblatt:
das logo (im anhang)
schriftzug: mira beauty schule
eventuell bild kussmund, wenn rechte vorhanden.
zweite spalte/hinterseite:
zahlungsbedingungen (text wird noch beigefügt)
dritte spalte:
personenbild (anhang)
personenbeschreibung (text wird noch beigefügt)
innenseite:
text aus anhang

```html
<!DOCTYPE html>
<html lang="de">
<head>
<meta charset="utf-8">
<title>mira beauty schule – make up ausbildung</title>
<link rel="stylesheet" href="https://fonts.googleapis.com/css2?family=Comfortaa:wght@400;700&family=Carlito:ital,wght@0,400;0,700;1,400&display=swap">
<style>
  :root {
    --bg: #000000;
    --ink: #ffffff;
    --magenta: #c4146e;
    --gold: #c98f1c;
    --photo-lips-a: #e8b9a6;
    --photo-lips-b: #b8736a;
    --photo-eye-a: #e9dccf;
    --photo-eye-b: #8c7466;
    --photo-eye2-a: #efe2cf;
    --photo-eye2-b: #b89f82;
  }
  * { box-sizing: border-box; margin: 0; padding: 0; }
  html, body { width: 1200px; height: 848px; overflow: hidden; background: var(--bg); }
  .sheet {
    position: relative; width: 1200px; height: 848px; background: var(--bg);
    color: var(--ink); font-family: "Carlito", "Calibri", sans-serif;
    font-size: 11.8px; line-height: 17.3px; overflow: hidden;
  }
  .fold-mark { position: absolute; left: 381px; top: 0; width: 5px; height: 140px; background: var(--magenta); }
  .accent-line { position: absolute; left: 1038px; top: 752px; width: 162px; height: 5px; background: var(--magenta); }
  .accent-block { position: absolute; left: 1113px; top: 736px; width: 71px; height: 10px; background: var(--ink); }

  .course { position: absolute; top: 0; height: 848px; }
  .course--basic { left: 32px; width: 330px; }
  .course--junior { left: 431px; width: 336px; }
  .course--senior { left: 831px; width: 332px; }

  .course-head { position: absolute; top: 35px; left: 0; display: flex; align-items: center; }
  .thumb { width: 68px; height: 45px; border: 2px solid #e9e9e9; flex: none; }
  .thumb--lips { background: radial-gradient(ellipse at 50% 55%, var(--photo-lips-b), var(--photo-lips-a) 70%); }
  .thumb--eye { background: linear-gradient(160deg, var(--photo-eye-a), var(--photo-eye-b)); }
  .thumb--eye-closed { background: linear-gradient(160deg, var(--photo-eye2-a), var(--photo-eye2-b)); }
  .course-title {
    font-family: "Comfortaa", sans-serif; font-weight: 400; font-size: 20px;
    letter-spacing: -0.4px; margin-left: 16px; margin-top: 6px; white-space: nowrap;
  }
  .course-title small { font-size: 9.5px; margin-left: 1px; letter-spacing: 0; }

  .intro { position: absolute; top: 101px; left: 0; right: 0; }
  .intro p + p { margin-top: 3px; }

  .label { font-weight: 700; font-size: 13px; line-height: 16px; }
  .label--magenta { color: var(--magenta); }
  .label--gold { color: var(--gold); }
  .label--white { color: var(--ink); }

  .topics { position: absolute; left: 0; right: 0; }
  .course--basic .topics { top: 163px; }
  .course--junior .topics { top: 196px; }
  .course--senior .topics { top: 254px; }
  .topics ul { list-style: none; margin-top: 9px; }
  .topics li { font-style: italic; position: relative; padding-left: 20px; line-height: 20px; }
  .topics li small { font-style: normal; font-size: 10px; }
  .topics li::before {
    content: ""; position: absolute; left: 0; top: 4px; width: 6px; height: 11px; background: var(--gold);
  }
  .topics li:nth-child(even)::before { background: var(--magenta); }
  .topics .note { display: block; padding-left: 110px; font-style: normal; font-size: 10px; }

  .dates { position: absolute; top: 404px; left: 0; right: 0; }
  .dates table { border-collapse: collapse; margin-top: 13px; font-style: italic; }
  .dates td { padding: 0; line-height: 17.2px; height: 17.2px; white-space: nowrap; }
  .dates td.day { width: 73px; padding-left: 20px; position: relative; }
  .dates td.day::before {
    content: ""; position: absolute; left: 0; top: 3px; width: 6px; height: 11px; background: var(--gold);
  }
  .dates tr:nth-child(even) td.day::before { background: var(--magenta); }
  .dates td.date { width: 100px; }

  .details { position: absolute; top: 592px; left: 0; right: 0; }
  .details .req { margin-top: 4px; line-height: 15.2px; }
  .details .cost { margin-top: 22px; }
  .course--senior .details .cost { margin-top: 14px; }
  .price { font-size: 21px; line-height: 26px; margin-top: 4px; }
  .price small { font-size: 9.5px; }
  .details .signup { margin-top: 18px; }
  .course--senior .details .signup { margin-top: 16px; }
  .signup p { margin-top: 6px; line-height: 14px; font-size: 11.4px; }
  .signup .line { white-space: nowrap; }
  .signup .tab { display: inline-block; width: 102px; }
  .course--senior .signup .tab { width: 90px; }
  .signup .discount { text-align: justify; }
</style>
</head>
<body>
<main class="sheet">
  <div class="fold-mark"></div>

  <section class="course course--basic">
    <header class="course-head">
      <div class="thumb thumb--lips" role="img" aria-label="Foto: geschminkter Mund in Nahaufnahme"></div>
      <h2 class="course-title">basic education <small>teil 1</small></h2>
    </header>
    <div class="intro">
      <p>in diesem workshop wird basiswissen vermittelt, mit dem jeder friseur professionell sein beauty-salonprogramm abrunden und das sortiment seiner dienstleistungen erweitern kann.</p>
    </div>
    <div class="topics">
      <h3 class="label label--magenta">inhalte auf einen blick:</h3>
      <ul>
        <li>produktwissen</li>
        <li>gesichtsvermessungen</li>
        <li>optimierung der gesichtsformen</li>
        <li>augenmakeups</li>
        <li>makeup für verschiedene augenformen</li>
        <li>augenmakeup für brillenträgerinnen</li>
        <li>tages-makeup</li>
        <li>abend-makeup</li>
        <li>special-makeup &nbsp;&nbsp;&nbsp;&nbsp;&nbsp;&nbsp;&nbsp;<small>(wimpern kleben, aufbringen von</small><span class="note">glitter und accessoires)</span></li>
      </ul>
    </div>
    <div class="dates">
      <h3 class="label label--gold">termine:</h3>
      <table>
        <tr><td class="day">so.,</td><td class="date">08.05.2011</td><td>10-18 uhr</td></tr>
        <tr><td class="day">mo.,</td><td class="date">09.05.2011</td><td>10-14 uhr</td></tr>
        <tr><td class="day">so.,</td><td class="date">15.05.2011</td><td>10-18 uhr</td></tr>
        <tr><td class="day">mo.,</td><td class="date">16.05.2011</td><td>10-14 uhr</td></tr>
        <tr><td class="day">so.,</td><td class="date">22.05.2011</td><td>10-18 uhr</td></tr>
        <tr><td class="day">mo.,</td><td class="date">23.05.2011</td><td>10-14 uhr</td></tr>
        <tr><td class="day">so.,</td><td class="date">29.05.2011</td><td>10-18 uhr</td></tr>
        <tr><td class="day">mo.,</td><td class="date">30.05.2011</td><td>10-14 uhr</td></tr>
      </table>
    </div>
    <div class="details">
      <h3 class="label label--white">vorraussetzungen:</h3>
      <p class="req">dieser kurs ist geeignet für einsteiger und für alle, die vorhandenes wissen auffrischen oder vertiefen wollen.</p>
      <div class="cost">
        <h3 class="label label--magenta">kosten:</h3>
        <p class="price">€ 990 <small>exkl. mwst</small></p>
      </div>
      <div class="signup">
        <h3 class="label label--gold">anmeldung:</h3>
        <p class="line"><span class="tab">bis 15.04.2011 :</span>mira@glanz.example oder unter 01 000 47 11</p>
      </div>
    </div>
  </section>

  <section class="course course--junior">
    <header class="course-head">
      <div class="thumb thumb--eye" role="img" aria-label="Foto: geschminktes Auge mit Wimpern"></div>
      <h2 class="course-title">junior make up artist <small>teil 2</small></h2>
    </header>
    <div class="intro">
      <p>junior makeup artists, die diesen kurs absolviert haben, sind in der lage, makeup- und typberatung, foto- und anti-aging-makeup anzubieten. die inhalte befassen sich noch detaillierter als im ersten teil mit farben und formen beim schminken und die techniken werden von der beratung bis zur umsetzung trainiert.</p>
    </div>
    <div class="topics">
      <h3 class="label label--magenta">inhalte auf einen blick:</h3>
      <ul>
        <li>haut</li>
        <li>anti-aging makeup</li>
        <li>foto-makeup</li>
        <li>schwarz/weiß foto-makeup</li>
        <li>männer-makeup</li>
        <li>typberatung</li>
        <li>makeupberatung</li>
        <li>braut-makeup</li>
      </ul>
    </div>
    <div class="dates">
      <h3 class="label label--gold">termine:</h3>
      <table>
        <tr><td class="day">so.,</td><td class="date">10.07.2011</td><td>10-18 uhr</td></tr>
        <tr><td class="day">mo.,</td><td class="date">11.07.2011</td><td>10-14 uhr</td></tr>
        <tr><td class="day">so.,</td><td class="date">17.07.2011</td><td>10-18 uhr</td></tr>
        <tr><td class="day">mo.,</td><td class="date">18.07.2011</td><td>10-14 uhr</td></tr>
        <tr><td class="day">so.,</td><td class="date">24.07.2011</td><td>10-18 uhr</td></tr>
        <tr><td class="day">mo.,</td><td class="date">25.07.2011</td><td>10-14 uhr</td></tr>
        <tr><td class="day">so.,</td><td class="date">31.07.2011</td><td>10-18 uhr</td></tr>
        <tr><td class="day">mo.,</td><td class="date">01.08.2011</td><td>10-14 uhr</td></tr>
      </table>
    </div>
    <div class="details">
      <h3 class="label label--white">vorraussetzungen:</h3>
      <p class="req">dieser kurs ist geeignet für friseure mit basiswissen, talentierte quereinsteiger und teilnehmer des ersten kurses, makeup basics. teilnehmer von makeup basics erhalten nach diesem kurs auch das junior makeup artist diplom</p>
      <div class="cost">
        <h3 class="label label--magenta">kosten:</h3>
        <p class="price">€ 990 <small>exkl. mwst</small></p>
      </div>
      <div class="signup">
        <h3 class="label label--gold">anmeldung:</h3>
        <p class="line"><span class="tab">bis 17.05.2011:</span>mira@glanz.example oder unter 01 000 47 11</p>
      </div>
    </div>
  </section>

  <section class="course course--senior">
    <header class="course-head">
      <div class="thumb thumb--eye-closed" role="img" aria-label="Foto: geschlossenes geschminktes Auge"></div>
      <h2 class="course-title">senior make up artist <small>teil 3</small></h2>
    </header>
    <div class="intro">
      <p>in dir steckt ein künstler? du spielst gerne mit farben und formen? möchtest schminken für große bühnenshows und extravagante fotoshootings? dann solltest du unbedingt auch den dritten teil dieser visagistenausbildung absolvieren.</p>
      <p>hier lernst du makeups verschiedener epochen zu schminken aber auch abzuwandeln. in diesem workshop nehmen wir uns besonders viel zeit techniken zu perfektionieren und deiner makeupkunst eine individuelle note zu geben.</p>
    </div>
    <div class="topics">
      <h3 class="label label--magenta">inhalte auf einen blick:</h3>
      <ul>
        <li>epochen makeup</li>
        <li>verschiedene kulturen/historische makeps <small>(20er bis 90er)</small></li>
        <li>geschichte des makeup</li>
        <li>laufsteg makeup <small>(geisha, orientalisches makeup, ...)</small></li>
        <li>x-treme makeup/phantasie-makeup</li>
      </ul>
    </div>
    <div class="dates">
      <h3 class="label label--gold">termine:</h3>
      <table>
        <tr><td class="day">so.,</td><td class="date">11.09.2011</td><td>10-18 uhr</td></tr>
        <tr><td class="day">mo.,</td><td class="date">12.09.2011</td><td>10-14 uhr</td></tr>
        <tr><td class="day">so.,</td><td class="date">18.09.2011</td><td>10-18 uhr</td></tr>
        <tr><td class="day">mo.,</td><td class="date">19.09.2011</td><td>10-14 uhr</td></tr>
        <tr><td class="day">so.,</td><td class="date">25.09.2011</td><td>10-18 uhr</td></tr>
        <tr><td class="day">mo.,</td><td class="date">26.09.2011</td><td>10-14 uhr</td></tr>
        <tr><td class="day">so.,</td><td class="date">02.10.2011</td><td>10-18 uhr</td></tr>
        <tr><td class="day">mo.,</td><td class="date">03.10.2011</td><td>10-14 uhr</td></tr>
      </table>
    </div>
    <div class="details">
      <h3 class="label label--white">vorraussetzungen:</h3>
      <p class="req">dieser kurs ist geeignet für kreative künstler mit vorbildung und rundet die ausbildung für teilnehmer von teil 1 und 2 (makeup basics und junior makeup artist) perfekt ab. der kurs endet mit einer schriftlichen und praktischen prüfung. teilnehmer, die auch die ersten beiden kurse besucht haben, erhalten nach bestandener prüfung ein visagistendiplom.</p>
      <div class="cost">
        <h3 class="label label--magenta">kosten:</h3>
        <p class="price">€ 990 <small>exkl. mwst</small></p>
      </div>
      <div class="signup">
        <h3 class="label label--gold">anmeldung:</h3>
        <p><span class="line"><span class="tab">bis 15.07.2011:</span>mira@glanz.example oder unter 01 000 47 11</span><br><span class="discount">bei anmeldung für alle drei kurse bis 01.03.2011, werden 5% rabatt auf den gesamtpreis gewährt.</span></p>
      </div>
    </div>
  </section>

  <div class="accent-block"></div>
  <div class="accent-line"></div>
</main>
</body>
</html>
```